Create Lanternfield HR Business Cards.

Create Business Cards for Lanternfield HR. 2 sided and Would like the back to have the logo.

Info for Business Card:
Address: 4827 Millbrook Ave Suite 230 Cleveland, Ohio 44987
Office Number: 216-555-0143
Mobile: 216-555-0192

Website: www.lanternfieldhr.example

Target Market(s)

Small to medium size businesses

Industry/Entity Type

Human Resources

Contact Information for Business Card

Company logo and information

Font styles to use
Serif
Sans Serif

Requirements
Must have
• Info for Business Card: Address: 4827 Millbrook Ave Suite 230 Cleveland, Ohio 44987 Office Number: 216-555-0143 Mobile: 216-555-0192 Website: www.lanternfieldhr.example

```html
<!DOCTYPE html>
<html lang="en">
<head>
<meta charset="utf-8">
<title>Lanternfield HR — Business Cards</title>
<link rel="stylesheet" href="https://fonts.googleapis.com/css2?family=Poppins:wght@400;500;600;700&display=swap">
<style>
  :root {
    --navy: #241f5e;
    --orange: #f7860d;
    --card-white: #ffffff;
    --card-black: #161718;
    --pattern-dark: #222325;
    --pattern-light: #3a3b3e;
    --rule: #9a9a9a;
    --stage: #e9e9eb;
  }
  * { box-sizing: border-box; margin: 0; padding: 0; }
  html, body { width: 1200px; height: 1108px; overflow: hidden; }
  body {
    background: var(--stage);
    font-family: "Poppins", sans-serif;
    position: relative;
  }
  .card {
    position: absolute;
    top: 204px;
    width: 400px;
    height: 700px;
    border-radius: 22px;
    overflow: hidden;
    box-shadow: 0 10px 30px rgba(0,0,0,0.18);
  }
  .card-front { left: 150px; background: var(--card-white); }
  .card-back { left: 650px; background: var(--card-black); }

  .brand {
    position: absolute;
    top: 150px; left: 0; right: 0;
    display: flex; align-items: center; justify-content: center; gap: 12px;
  }
  .brand-dot { width: 34px; height: 34px; border-radius: 50%; background: var(--orange); }
  .brand-name { color: var(--navy); font-weight: 700; font-size: 32px; letter-spacing: 0.5px; }

  .person { position: absolute; top: 330px; left: 0; right: 0; text-align: center; }
  .person-name { color: var(--navy); font-weight: 700; font-size: 26px; letter-spacing: 1px; text-transform: uppercase; line-height: 1.1; }
  .person-title { color: var(--orange); font-weight: 400; font-size: 20px; line-height: 1.2; }

  .icon-row {
    position: absolute; top: 412px; left: 40px; right: 40px;
    display: flex; align-items: center; gap: 8px;
  }
  .icon-row .rule { flex: 1; height: 1px; background: var(--rule); }
  .icon-box {
    width: 32px; height: 32px; border-radius: 5px; background: var(--navy);
    display: flex; align-items: center; justify-content: center;
  }

  .contact { position: absolute; top: 462px; left: 0; right: 0; text-align: center; color: var(--navy); font-size: 19px; line-height: 1.4; }
  .contact .web-accent { color: var(--orange); }
  .divider { position: absolute; top: 560px; left: 40px; right: 40px; height: 1px; background: var(--rule); }
  .address { position: absolute; top: 578px; left: 0; right: 0; text-align: center; color: var(--navy); font-size: 18px; line-height: 1.4; }

  .back-pattern {
    position: absolute; inset: 0;
    background: linear-gradient(200deg, var(--pattern-light) 0%, var(--pattern-dark) 45%, var(--card-black) 100%);
  }
  .back-brand {
    position: absolute; right: 34px; bottom: 190px;
    display: flex; align-items: center; gap: 7px;
  }
  .back-brand .brand-dot { width: 16px; height: 16px; }
  .back-brand .brand-name { color: var(--card-white); font-size: 15px; }
</style>
</head>
<body>
  <section class="card card-front" aria-label="Business card front">
    <div class="brand">
      <span class="brand-dot"></span>
      <span class="brand-name">Lanternfield HR</span>
    </div>

    <div class="person">
      <p class="person-name">Marcus Ellery</p>
      <p class="person-title">Managing Director</p>
    </div>

    <div class="icon-row">
      <span class="rule"></span>
      <span class="icon-box" aria-label="Phone">
        <svg width="18" height="18" viewBox="0 0 24 24"><path fill="#fff" d="M6.6 10.8a15.1 15.1 0 0 0 6.6 6.6l2.2-2.2a1 1 0 0 1 1-.25 11.4 11.4 0 0 0 3.6.57 1 1 0 0 1 1 1V20a1 1 0 0 1-1 1A17 17 0 0 1 3 4a1 1 0 0 1 1-1h3.5a1 1 0 0 1 1 1c0 1.25.2 2.45.57 3.6a1 1 0 0 1-.25 1z"/></svg>
      </span>
      <span class="icon-box" aria-label="Email">
        <svg width="18" height="18" viewBox="0 0 24 24"><rect x="3" y="5" width="18" height="14" rx="1" fill="none" stroke="#fff" stroke-width="2"/><path d="M3 6l9 7 9-7" fill="none" stroke="#fff" stroke-width="2"/></svg>
      </span>
      <span class="icon-box" aria-label="Website">
        <svg width="18" height="18" viewBox="0 0 24 24"><circle cx="12" cy="12" r="9" fill="none" stroke="#fff" stroke-width="2"/><path d="M3 12h18M12 3c3 3 3 15 0 18M12 3c-3 3-3 15 0 18" fill="none" stroke="#fff" stroke-width="1.5"/></svg>
      </span>
      <span class="rule"></span>
    </div>

    <div class="contact">
      <p>216-555-0143</p>
      <p>216-555-0192</p>
      <p>www.<span class="web-accent">lanternfieldhr</span>.example</p>
    </div>

    <div class="divider"></div>

    <div class="address">
      <p>4827 Millbrook Ave Suite</p>
      <p>230 Cleveland, Ohio 44987</p>
    </div>
  </section>

  <section class="card card-back" aria-label="Business card back">
    <div class="back-pattern" role="img" aria-label="Repeating tone-on-tone brand pattern in glossy black and grey"></div>
    <div class="back-brand">
      <span class="brand-dot"></span>
      <span class="brand-name">Lanternfield HR</span>
    </div>
  </section>
</body>
</html>
```